Bright Arc Electrical & Communications business card design

We would like a double sided business card that is different. Want it to be exciting and fun. Something that people keep rather then just throw it in the bin.
We have a logo that we want to put on one side of the business card and then the business information on the reverse side. Trying to go for a real professional style of business card

Target Market(s)

Electrical

Industry/Entity Type

Electrical

Contact Information for Business Card

Bright Arc Electrical & Communications
Marcus Trelowen
P: 0437 286 354
E: brightarc@mailrove.com.au
Lic No: 547106K
24/7

Font styles to use
Other font styles liked:
• Would like ideas

Requirements
Must have
• Our company logo (preferably on both sides) yellow needs to be incorporated somewhere. Business card card colours to match with logo. Maybe a small pop of colour
Nice to have
• Open to some design ideas

```html
<!DOCTYPE html>
<html lang="en">
<head>
<meta charset="utf-8">
<title>Bright Arc Electrical &amp; Communications – Business Card</title>
<link href="https://fonts.googleapis.com/css2?family=Michroma&display=swap" rel="stylesheet">
<style>
  :root {
    --backdrop: #3a332f;
    --card: #050505;
    --card-edge: #1a1a1a;
    --silver: #bdbdbd;
    --white: #f2f2f2;
    --yellow: #f2e21b;
    --emblem-grey: #8a8a8a;
    --ink: #0b0b0b;
  }
  * { margin: 0; padding: 0; box-sizing: border-box; }
  html, body { width: 1200px; height: 780px; overflow: hidden; }
  body {
    background: var(--backdrop);
    font-family: "Michroma", sans-serif;
    position: relative;
  }
  .card {
    position: absolute;
    top: 235px;
    width: 540px;
    height: 310px;
    background: var(--card);
    border: 1px solid var(--card-edge);
    border-radius: 4px;
    box-shadow: 0 14px 30px rgba(0,0,0,.45);
    overflow: hidden;
  }
  .card--front { left: 45px; }
  .card--back { left: 615px; }

  .emblem-area { position: absolute; border-radius: 50%; }
  .card--front .emblem-area {
    left: 140px; top: 25px; width: 260px; height: 260px;
    background: radial-gradient(circle, rgba(70,70,60,.35) 0%, rgba(40,40,35,.25) 55%, rgba(5,5,5,0) 72%);
  }
  .card--back .emblem-area {
    left: 385px; top: 160px; width: 135px; height: 135px;
    background: radial-gradient(circle, rgba(242,226,27,.55) 0%, rgba(242,226,27,.25) 35%, rgba(138,138,138,.35) 60%, rgba(5,5,5,0) 72%);
  }

  .brand { position: absolute; display: flex; align-items: center; gap: 16px; z-index: 1; }
  .brand__dot {
    width: 22px; height: 22px; border-radius: 50%;
    background: var(--yellow); flex: none;
  }
  .brand__name {
    color: var(--silver);
    font-size: 30px;
    line-height: 1.2;
    letter-spacing: 1px;
    text-transform: uppercase;
    white-space: nowrap;
  }
  .brand__tag {
    position: absolute; z-index: 1;
    color: var(--white); letter-spacing: 1px;
    text-transform: uppercase; white-space: nowrap;
  }
  .brand__rule { position: absolute; height: 1px; background: var(--yellow); z-index: 1; }

  .card--front .brand { left: 70px; top: 100px; }
  .card--front .brand__tag { left: 108px; top: 180px; font-size: 13px; }
  .card--front .brand__rule { left: 108px; top: 206px; width: 360px; }

  .card--back .brand { left: 34px; top: 38px; }
  .card--back .brand__name { font-size: 22px; }
  .card--back .brand__dot { width: 16px; height: 16px; }
  .card--back .brand__tag { left: 66px; top: 100px; font-size: 10px; }
  .card--back .brand__rule { left: 66px; top: 120px; width: 270px; }

  .licence {
    position: absolute; right: 30px; top: 44px;
    color: var(--white); font-size: 12px; letter-spacing: 1px; white-space: nowrap;
  }
  .person {
    position: absolute; left: 34px; top: 150px;
    color: var(--white); font-size: 22px; letter-spacing: 1px; white-space: nowrap;
  }
  .contact { position: absolute; left: 34px; top: 200px; list-style: none; }
  .contact__item {
    display: flex; align-items: center; gap: 12px;
    color: var(--white); font-size: 12.5px; letter-spacing: .5px;
    margin-bottom: 12px; white-space: nowrap;
  }
  .contact__icon {
    width: 18px; height: 18px; background: var(--yellow);
    display: flex; align-items: center; justify-content: center; flex: none;
  }
</style>
</head>
<body>

  <section class="card card--front" aria-label="Business card front">
    <div class="emblem-area" role="img" aria-label="Faint company emblem watermark"></div>
    <div class="brand">
      <span class="brand__dot"></span>
      <span class="brand__name">Bright Arc</span>
    </div>
    <p class="brand__tag">Electrical &amp; Communications</p>
    <span class="brand__rule"></span>
  </section>

  <section class="card card--back" aria-label="Business card back">
    <div class="brand">
      <span class="brand__dot"></span>
      <span class="brand__name">Bright Arc</span>
    </div>
    <p class="brand__tag">Electrical &amp; Communications</p>
    <span class="brand__rule"></span>

    <p class="licence">Lic No: 547106K</p>
    <p class="person">Marcus Trelowen</p>

    <ul class="contact">
      <li class="contact__item">
        <span class="contact__icon">
          <svg width="12" height="12" viewBox="0 0 24 24" aria-hidden="true">
            <path fill="#0b0b0b" d="M6.6 10.8a15.1 15.1 0 0 0 6.6 6.6l2.2-2.2c.3-.3.7-.4 1-.2 1.1.4 2.3.6 3.6.6.6 0 1 .4 1 1V20c0 .6-.4 1-1 1C10.6 21 3 13.4 3 4c0-.6.4-1 1-1h3.5c.6 0 1 .4 1 1 0 1.3.2 2.5.6 3.6.1.3 0 .7-.2 1z"/>
          </svg>
        </span>
        0437 286 354
      </li>
      <li class="contact__item">
        <span class="contact__icon">
          <svg width="12" height="12" viewBox="0 0 24 24" aria-hidden="true">
            <rect x="2" y="5" width="20" height="14" fill="none" stroke="#0b0b0b" stroke-width="2.4"/>
            <path d="M2 5l10 8 10-8" fill="none" stroke="#0b0b0b" stroke-width="2.4"/>
          </svg>
        </span>
        brightarc@mailrove.com.au
      </li>
    </ul>

    <div class="emblem-area" role="img" aria-label="Company emblem in yellow and grey"></div>
  </section>

</body>
</html>
```